Larkspur Elementary
Stationary, Letterhead, Business Card
Simple
Cora P. Wendt
Counselor
742 Ridgeway Lane
Alder Creek, CO 80999
wendt_cora@mbxsd.org
http://les.hollowmere.k12.xx.us
I would like to stay with the navy gold and blue theme (but variations are fine) but a white background is not necessary.
I like the vertical look more than the horizontal but both are welcomed.
If you follow the link, I like how #8, #15, and #18 look format-wise.
I look forward to your designs.
http://www.quarvelblog.com/2008/06/25/yet-another-post-with-unique-business-cards/
Logo plus your creative touches

```html
<!DOCTYPE html>
<html lang="en">
<head>
<meta charset="utf-8">
<title>Larkspur Elementary Counseling – Business Card</title>
<link href="https://fonts.googleapis.com/css2?family=Open+Sans:wght@400;600;700;800&display=swap" rel="stylesheet">
<style>
  :root{
    --stage:#3b1616;
    --card:#ffffff;
    --gold:#d9a21f;
    --gold-deep:#b07a12;
    --navy:#1f3f7a;
    --blue:#2f5fa3;
    --blue-light:#b9cbe2;
    --silver:#d7d9dc;
    --ink:#1c1c1c;
    --white:#ffffff;
  }
  *{box-sizing:border-box;margin:0;padding:0}
  html,body{width:1200px;height:901px;overflow:hidden}
  body{background:var(--stage);font-family:"Open Sans",Arial,sans-serif;position:relative}
  .card{position:absolute;width:353px;height:616px;background:var(--card);overflow:hidden;
        box-shadow:0 6px 18px rgba(0,0,0,.45)}
  .card--front{left:195px;top:80px}
  .card--back{left:650px;top:195px}
  .card__waves{position:absolute;inset:0;width:100%;height:100%}

  .brand{position:absolute;left:26px;top:26px;display:flex;align-items:center;gap:10px}
  .brand__mark{width:46px;height:46px;background:var(--gold);flex:none}
  .brand__name{color:var(--gold-deep);font-weight:800;font-size:17px;line-height:1.05;text-transform:uppercase;letter-spacing:.2px}
  .brand__tagline{position:absolute;left:82px;top:80px;color:var(--navy);font-size:9.5px;font-weight:600;letter-spacing:.6px;text-transform:uppercase}

  .nameplate{position:absolute;left:78px;top:290px;width:200px;height:150px;border-radius:14px;
             background:linear-gradient(135deg,#f2c85a,var(--gold) 50%,var(--gold-deep));
             display:flex;flex-direction:column;justify-content:center;align-items:center;
             box-shadow:0 3px 8px rgba(0,0,0,.2)}
  .nameplate__name{font-size:19px;font-weight:700;color:var(--ink)}
  .nameplate__title{font-size:13px;color:var(--ink);margin-top:4px}

  .contact{position:absolute;left:0;right:0;top:488px;color:var(--white);font-size:11.5px;text-align:center;line-height:1.5}
  .contact__list{margin-top:12px;display:inline-grid;grid-template-columns:auto auto;column-gap:14px;text-align:left}

  .back__emblem{position:absolute;left:110px;top:60px;width:140px;height:140px;
                background:var(--gold);box-shadow:0 4px 10px rgba(0,0,0,.25)}
  .back__url{position:absolute;left:0;right:0;top:578px;text-align:center;color:var(--white);font-size:14px;font-weight:600}
</style>
</head>
<body>

<section class="card card--front" aria-label="Business card front">
  <svg class="card__waves" viewBox="0 0 353 616" preserveAspectRatio="none" aria-hidden="true">
    <defs>
      <linearGradient id="silverFront" x1="0" y1="0" x2="1" y2="1">
        <stop offset="0" stop-color="#f4f4f5"/><stop offset=".5" stop-color="#cfd2d6"/><stop offset="1" stop-color="#f7f7f8"/>
      </linearGradient>
      <linearGradient id="blueFront" x1="0" y1="0" x2="1" y2="0">
        <stop offset="0" stop-color="#2a589c"/><stop offset=".6" stop-color="#3f6fb0"/><stop offset="1" stop-color="#b9cbe2"/>
      </linearGradient>
    </defs>
    <path d="M0 250 C90 200 200 170 353 190 L353 470 C250 430 120 470 0 500 Z" fill="url(#silverFront)"/>
    <path d="M0 300 C120 240 230 250 353 230 L353 260 C230 290 120 280 0 340 Z" fill="#ffffff" opacity=".7"/>
    <path d="M0 470 C110 440 240 420 353 450 L353 616 L0 616 Z" fill="url(#blueFront)"/>
    <path d="M0 470 C110 440 240 420 353 450 L353 462 C240 436 110 456 0 486 Z" fill="#ffffff" opacity=".55"/>
  </svg>

  <div class="brand">
    <span class="brand__mark"></span>
    <span class="brand__name">Larkspur<br>Elementary Counseling</span>
  </div>
  <p class="brand__tagline">Promoting Lifelong Learning</p>

  <div class="nameplate">
    <p class="nameplate__name">Cora P. Wendt</p>
    <p class="nameplate__title">Counselor</p>
  </div>

  <div class="contact">
    <p>742 Ridgeway Lane<br>Alder Creek, CO 80999</p>
    <div class="contact__list">
      <span>Ph</span><span>: 555.014.2873</span>
      <span>Fax</span><span>: 555.014.2916</span>
      <span>Email</span><span>: wendt_cora@mbxsd.org</span>
    </div>
  </div>
</section>

<section class="card card--back" aria-label="Business card back">
  <svg class="card__waves" viewBox="0 0 353 616" preserveAspectRatio="none" aria-hidden="true">
    <defs>
      <linearGradient id="silverBack" x1="0" y1="0" x2="1" y2="1">
        <stop offset="0" stop-color="#f6f6f7"/><stop offset=".5" stop-color="#cdd0d4"/><stop offset="1" stop-color="#f4f4f5"/>
      </linearGradient>
      <linearGradient id="blueBack" x1="0" y1="0" x2="1" y2="0">
        <stop offset="0" stop-color="#2a589c"/><stop offset=".55" stop-color="#3d6db0"/><stop offset="1" stop-color="#c3d3e7"/>
      </linearGradient>
    </defs>
    <path d="M0 160 C100 110 220 140 353 120 L353 420 C240 380 110 380 0 420 Z" fill="url(#silverBack)"/>
    <path d="M0 230 C120 170 240 200 353 170 L353 200 C240 230 120 210 0 270 Z" fill="#ffffff" opacity=".7"/>
    <path d="M0 380 C120 340 250 360 353 330 L353 616 L0 616 Z" fill="url(#blueBack)"/>
    <path d="M0 380 C120 340 250 360 353 330 L353 344 C250 374 120 356 0 396 Z" fill="#ffffff" opacity=".55"/>
  </svg>

  <div class="back__emblem"></div>
  <p class="back__url">www.les.hollowmere.k12.xx.us</p>
</section>

</body>
</html>
```